Summer Sunglass offer

Need a poster design for a spring / summer campaign. We are an opticians with good footfall. The design needs to be eye catching and aimed at 40 year old plus. The offer is Up to 50% off sunglass offer, t&c apply. (I have attached our last year campaign)
Also need a 2 sided A5 leaflet design (see attached)
I've uploaded a copy of our logo

A5 leaflet should read:

Grab a bargain on two great looks this summer Upto 50% off sunglasses
Look great and stay safe in the sun this summer

We want you to look great, feel fantastic and most of all stay safe in the sun this summer. That’s why we’re offering you 50% off prescription sunglasses with every complete pair of glasses you buy this summer or 25% off for prescription sunglasses with no other purchase.
Find you new summer looks from our gorgeous collection of frames in store. It matters to us that you look great in your new glasses as much as how well you see through them, so we’ll be on hand to help you find frames that suit you best.
What new looks will you go for? Smart or sassy? Formal or Fun? Whatever you’re in the mood for, you’ll find it in our collections this summer.
Call in today to find your new looks, and remember to bring your prescription if you don’t need an eye test.

Target Market(s)

40 + year old

Industry/Entity Type

Optician

Colors

Designer to choose colors to be used in the design.

Requirements
Must have
• Images, preferably a male and Female image

```html
<!DOCTYPE html>
<html lang="en">
<head>
<meta charset="utf-8">
<title>Summer Sunglasses Offer</title>
<link href="https://fonts.googleapis.com/css2?family=Libre+Franklin:wght@400;500;600&family=Varela+Round&family=Archivo+Black&display=swap" rel="stylesheet">
<style>
  :root {
    --green: #259b74;
    --green-light: #43ac89;
    --green-dark: #1f5f52;
    --mint: #4dd4ac;
    --ink: #3a3a3a;
    --white: #ffffff;
    --photo-warm: #d9b79a;
    --photo-cool: #6aa3a0;
  }
  * { margin: 0; padding: 0; box-sizing: border-box; }
  html, body { width: 846px; height: 1200px; overflow: hidden; background: var(--white); }
  .leaflet { position: relative; width: 846px; height: 1200px; background: var(--white); font-family: "Libre Franklin", sans-serif; color: var(--ink); }

  .hero-photo { position: absolute; left: 0; top: 0; width: 846px; height: 648px;
    background: linear-gradient(135deg, #f4f1ec 0%, #e8d3bd 30%, var(--photo-warm) 50%, var(--photo-cool) 75%, #e9c9cc 100%); }

  .brand { display: flex; align-items: center; gap: 8px; font-family: "Libre Franklin", sans-serif; font-weight: 600; color: var(--green); }
  .brand .dot { width: 14px; height: 14px; border-radius: 50%; background: var(--green); }
  .brand-top { position: absolute; top: 42px; right: 34px; font-size: 20px; }
  .brand-bottom { position: absolute; left: 68px; top: 1098px; font-size: 26px; }
  .brand-bottom .dot { width: 20px; height: 20px; }

  .headline-panel { position: absolute; left: 502px; top: 134px; width: 344px; height: 208px; background: var(--green-light); opacity: .97;
    font-family: "Varela Round", sans-serif; color: var(--white); font-size: 35px; line-height: 44px; text-align: center; padding-top: 40px; padding-left: 24px; }
  .offer-panel { position: absolute; left: 548px; top: 323px; width: 298px; height: 170px; background: var(--green-dark);
    font-family: "Varela Round", sans-serif; color: var(--white); font-size: 34px; line-height: 44px; padding: 52px 0 0 26px; }
  .offer-panel strong { font-family: "Archivo Black", sans-serif; font-weight: 400; font-size: 33px; }

  .title-band { position: absolute; left: 0; top: 490px; width: 518px; height: 182px; background: var(--green);
    color: var(--white); font-family: "Libre Franklin", sans-serif; font-weight: 500; font-size: 34px; line-height: 42px; padding: 52px 0 0 21px; letter-spacing: .2px; }

  .body { position: absolute; left: 47px; top: 688px; width: 760px; font-size: 17.4px; line-height: 24px; font-weight: 500; }
  .body p { text-align: justify; margin-bottom: 24px; }
  .questions { display: flex; gap: 0; color: var(--green); font-weight: 600; padding-left: 55px; margin: 2px 0 20px; }
  .questions span:nth-child(1) { width: 292px; }
  .questions span:nth-child(2) { width: 174px; }
  .cta { color: var(--green); font-weight: 600; }

  .phone { position: absolute; left: 456px; top: 1058px; font-size: 35px; font-weight: 600; color: var(--green); letter-spacing: .5px; }
  .address { position: absolute; left: 462px; top: 1108px; font-size: 18px; line-height: 24px; font-weight: 500; }
  .footer-bar { position: absolute; left: 0; bottom: 0; width: 846px; height: 12px; background: var(--green); }
</style>
</head>
<body>
<main class="leaflet">
  <div class="hero-photo" role="img" aria-label="Smiling couple wearing sunglasses on a sunny town street"></div>

  <div class="brand brand-top"><span class="dot"></span>Brookfield Vision Studio</div>

  <div class="headline-panel">Grab a bargain on two great looks this summer</div>
  <div class="offer-panel">Upto <strong>50% OFF</strong><br>sunglasses</div>

  <h1 class="title-band">LOOK GREAT AND STAY SAFE<br>IN THE SUN THIS SUMMER</h1>

  <section class="body">
    <p>We want you to look great, feel fantastic and most of all stay safe in the sun this summer. That’s why we’re offering you 50% off prescription sunglasses with every complete pair of glasses you buy this summer or 25% off for prescription sunglasses with no other purchase.</p>
    <p>Find you new summer looks from our gorgeous collection of frames in store. It matters to us that you love how you look in your new glasses as much as how well you see through them, so we’ll be on hand to help you find frames that suit you best.</p>
    <div class="questions"><span>What new looks will you go for?</span><span>Smart or sassy?</span><span>Formal or Fun?</span></div>
    <p>Whatever you’re in the mood for, you’ll find it in our collections this summer.</p>
    <p class="cta">Call in today to find your new looks, and remember to bring your prescription if you don’t need an eye test.</p>
  </section>

  <div class="brand brand-bottom"><span class="dot"></span>Brookfield Vision Studio</div>
  <div class="phone">+44 1632 960418</div>
  <div class="address">14 Market Row, Ashbury AB1 2CD,<br>United Kingdom</div>
  <div class="footer-bar"></div>
</main>
</body>
</html>
```